Banner for promote service of debit card

We are PagaVelo and we need the banners to be posted on the facebook and instagram pages.
We want something to communicate that it is an exclusive debit card full of services.
Low commissions.
Our competitors:
https://www.nortapay-pagos.it/it/home.html
https://www.zelkor-conti.it/it/
https://www.fotoreelz.it/serravanbank/
sendquillo
maybe some banner that makes the idea of a convenient debit card that everyone can use.
Girls enjoying card shopping.
Please check also website for slogans and phrases to use
https://www.pagavelo-carta.it/
Should show the services.
We must convey that it is a fast, simple card that guarantees privacy.
We need strong banners that attract people as these ban will be sponsored on instagram and facebook
Target Market(s)
People 18-35 y
Open Bank account. low commissions. Easy to use. No limits. 100% Privacy.
Requirements
Must have
- Written in Italian.

```html
<!DOCTYPE html>
<html lang="it">
<head>
<meta charset="utf-8">
<title>PagaVelo – Banner carta di debito</title>
<link rel="stylesheet" href="https://fonts.googleapis.com/css2?family=Poppins:wght@300;400;500;700;800&family=Bebas+Neue&display=swap">
<style>
  :root{
    --board:#3c3c3c;
    --white:#ffffff;
    --orange:#ff6a3d;
    --magenta:#be0f8c;
    --red:#ee3a46;
    --ink:#2a2a2a;
    --grey:#7d7d7d;
    --paper:#f4f4f4;
    --pink-soft:#f7b9c4;
    --wood:#e9c9a6;
  }
  *{margin:0;padding:0;box-sizing:border-box}
  html,body{width:713px;height:1200px;overflow:hidden;background:var(--board)}
  body{position:relative;font-family:"Poppins",sans-serif}

  .board-title{position:absolute;left:0;top:59px;width:713px;text-align:center;color:var(--white);
    font-size:16px;font-weight:400;letter-spacing:5.6px;white-space:nowrap}

  .sample-label{position:absolute;left:58px;color:var(--white);font-size:14px;letter-spacing:3.5px;
    transform:rotate(-90deg);transform-origin:left top;white-space:nowrap;font-weight:400}

  .banner{position:absolute;left:81px;width:572px;height:300px;overflow:hidden;background:var(--paper)}
  .banner > *{position:absolute;white-space:nowrap}

  .photo{top:0;height:300px}

  .brand{display:flex;align-items:center;gap:6px;color:var(--grey);font-weight:700}
  .brand-dot{width:.7em;height:.7em;border-radius:50%;background:var(--orange)}

  .headline{font-weight:800;color:var(--orange);letter-spacing:-2px;line-height:1}
  .band{background:linear-gradient(90deg,var(--magenta),var(--red));color:var(--white);display:flex;align-items:center;overflow:hidden}

  /* Banner 1 */
  .b1{top:136px;background:linear-gradient(90deg,#fafafa 0%,#fbeef0 45%,var(--pink-soft) 100%)}
  .b1 .photo{left:250px;width:322px;background:linear-gradient(90deg,rgba(248,214,220,.0),#e9b79c 30%,#f4c9cf 60%,#b8d8ee 85%,#f4a8b6)}
  .b1 .brand{left:28px;top:55px;font-size:17px}
  .b1 .headline{left:23px;top:93px;font-size:44px}
  .b1 .sub{left:87px;top:134px;font-size:14px;color:var(--magenta);font-weight:400}
  .b1 .band{left:23px;top:154px;width:222px;height:40px;font-size:40px;font-weight:800;letter-spacing:-1.5px;padding-left:8px}
  .b1 .features{left:30px;top:204px;list-style:none}
  .b1 .features li{display:flex;align-items:center;gap:9px;font-size:13px;color:var(--ink);height:20px}

  /* Banner 2 */
  .b2{top:487px;background:radial-gradient(circle at 75% 50%,#d9d9d9,#f3f3f3 70%)}
  .b2 .photo{left:322px;width:250px;background:linear-gradient(180deg,#9a5a36 0%,#e6b59a 35%,#e21d2a 70%,#e8b19a 100%)}
  .b2 .headline{left:25px;font-size:49px}
  .b2 .h-a{top:31px}
  .b2 .h-b{top:75px}
  .b2 .band{left:25px;top:125px;width:281px;height:51px;padding-left:7px;
    font-family:"Bebas Neue",sans-serif;font-size:44px;letter-spacing:0;line-height:1}
  .b2 .band-text{display:inline-block;transform:scaleX(.92);transform-origin:left center;padding-top:4px}
  .b2 .lead{left:24px;top:181px;font-size:27px;font-weight:300;color:var(--ink);letter-spacing:-.6px}
  .b2 .punch{left:24px;font-size:32px;font-weight:800;color:var(--magenta);letter-spacing:-1px;line-height:1}
  .b2 .p-a{top:213px}
  .b2 .p-b{top:246px}

  /* Banner 3 */
  .b3{top:837px;background:radial-gradient(circle at 78% 50%,#dedede,#f7f7f7 65%)}
  .b3 .photo{left:322px;width:228px;top:13px;height:287px;background:linear-gradient(180deg,#8c4a2c 0%,#eab59c 30%,#f1ece6 55%,#b9b9bd 70%,#2d4b7a 100%)}
  .b3 .brand{left:30px;top:74px;font-size:26px}
  .b3 .headline{left:32px;font-size:38px}
  .b3 .h-a{top:120px}
  .b3 .h-c{top:197px}
  .b3 .band{left:28px;top:155px;width:308px;height:38px;font-size:36px;font-weight:800;letter-spacing:-2px;padding-left:4px}
  .b3 .tagline{left:32px;top:240px;font-size:13px;color:var(--ink);letter-spacing:-.2px}
  .b3 .floor{left:0;top:272px;width:572px;height:28px;background:linear-gradient(90deg,#f1dcc4,var(--wood))}
  .b3 .site{left:30px;top:279px;font-size:11px;letter-spacing:2.6px;color:#4a3a30}
</style>
</head>
<body>
  <h1 class="board-title">BANNER FOR PROMOTE SERVICE OF DEBIT CARD</h1>

  <span class="sample-label" style="top:436px">SAMPLE 1</span>
  <span class="sample-label" style="top:787px">SAMPLE 2</span>
  <span class="sample-label" style="top:1137px">SAMPLE 3</span>

  <section class="banner b1">
    <div class="photo" role="img" aria-label="Due ragazze con cappello di paglia sorridono mostrando una carta di debito su fondo rosa"></div>
    <div class="brand"><span class="brand-dot"></span>PagaVelo</div>
    <h2 class="headline">ALL IN ONE!</h2>
    <p class="sub">UNA CARTA</p>
    <p class="band">PER TUTTI</p>
    <ul class="features">
      <li><svg width="10" height="10" viewBox="0 0 10 10"><circle cx="5" cy="5" r="4.2" fill="none" stroke="#be0f8c" stroke-width="1"/><path d="M3 5.1l1.4 1.4L7.1 3.8" fill="none" stroke="#be0f8c" stroke-width="1"/></svg>Enjoy your cart!</li>
      <li><svg width="10" height="10" viewBox="0 0 10 10"><circle cx="5" cy="5" r="4.2" fill="none" stroke="#be0f8c" stroke-width="1"/><path d="M3 5.1l1.4 1.4L7.1 3.8" fill="none" stroke="#be0f8c" stroke-width="1"/></svg>Fai quello che vuoi.</li>
      <li><svg width="10" height="10" viewBox="0 0 10 10"><circle cx="5" cy="5" r="4.2" fill="none" stroke="#be0f8c" stroke-width="1"/><path d="M3 5.1l1.4 1.4L7.1 3.8" fill="none" stroke="#be0f8c" stroke-width="1"/></svg>Nessun limite.</li>
      <li><svg width="10" height="10" viewBox="0 0 10 10"><circle cx="5" cy="5" r="4.2" fill="none" stroke="#be0f8c" stroke-width="1"/><path d="M3 5.1l1.4 1.4L7.1 3.8" fill="none" stroke="#be0f8c" stroke-width="1"/></svg>Nessun controllo.</li>
    </ul>
  </section>

  <section class="banner b2">
    <div class="photo" role="img" aria-label="Ragazza in top rosso sorride e mostra una carta di debito"></div>
    <p class="headline h-a">PRIVACY</p>
    <p class="headline h-b">GARANTITA</p>
    <p class="band"><span class="band-text">CREDITO ASSICURATO</span></p>
    <p class="lead">USALA COME VUOI</p>
    <p class="punch p-a">SENZA ESSERE</p>
    <p class="punch p-b">CONTROLLATO</p>
  </section>

  <section class="banner b3">
    <div class="floor"></div>
    <div class="photo" role="img" aria-label="Ragazza entusiasta seduta a gambe incrociate con un portatile e una carta di debito"></div>
    <div class="brand"><span class="brand-dot"></span>PagaVelo</div>
    <p class="headline h-a">VELOCE</p>
    <p class="band">INTERNAZIONALE</p>
    <p class="headline h-c">SEMPLICE.</p>
    <p class="tagline">ACQUISTA OVUNQUE SENZA LIMITI,</p>
    <p class="site">WWW.PAGAVELO-CARTA.IT</p>
  </section>
</body>
</html>
```